Graphic Design Project

ok I have the artwork for my presentation folder, and I have the text to put on the folder, I need you to apply text to the folder and the single sheets, so inside the artwork is pictures to use, text to use. thank you so much ask me as many questions as you need
Updates

my girl forgot to upload the mock ups of the presentation folder and single sheets, my apologies please check updated files

Hey Guys this is a eazy project the artwork is done, the text is done, the pictures are done!, all you have to do is assemble the project, I even have mock up pictures of how project looks finished, I have made the money good so that you would not pass on this project because it is not that creative of a job!

Target Market(s)

Dr's and patients

Industry/Entity Type

Graphic Design

Requirements
Must have
• use the single sheet artwork to make as many single sheets as you need to use all of the text supplied
Should not have
• do not make this, so professional looking that it does not appeal to the patients

```html
<!DOCTYPE html>
<html lang="en">
<head>
<meta charset="utf-8">
<title>CareWell Counseling – Presentation Folder Spread</title>
<link href="https://fonts.googleapis.com/css2?family=Tinos:ital,wght@0,400;0,700;1,400&display=swap" rel="stylesheet">
<style>
  :root {
    --backdrop: #e9e4dc;
    --paper: #ffffff;
    --brown: #714a27;
    --gray-panel: #d2d2d4;
    --beige-panel: #d9d0c0;
    --ink: #1a1a1a;
    --muted: #555555;
    --accent: #8a4513;
    --services-title: #5a5a5a;
  }
  * { margin: 0; padding: 0; box-sizing: border-box; }
  html, body {
    width: 1200px; height: 1000px; overflow: hidden;
    background: var(--backdrop);
    font-family: "Tinos", "Times New Roman", serif;
  }
  .folder {
    position: absolute; left: 12px; top: 132px;
    width: 1178px; height: 786px;
    background: var(--paper);
    overflow: hidden;
  }
  .folder-shapes { position: absolute; inset: 0; }
  .intro {
    position: absolute; left: 541px; top: 17px; width: 620px;
    font-size: 13px; line-height: 16px; color: var(--ink);
  }
  .intro strong { font-weight: 700; }
  .terms {
    position: absolute; left: 541px; top: 117px; width: 620px;
    font-size: 10.5px; line-height: 13.2px; color: var(--muted);
  }
  .terms .terms-heading { text-transform: uppercase; font-size: 11px; }
  .terms em { font-style: italic; }
  .education {
    position: absolute; left: 763px; top: 211px; width: 300px;
    color: var(--accent);
  }
  .education h2 { font-size: 15.5px; font-weight: 700; margin-left: 12px; margin-bottom: 12px; }
  .education ul { list-style: none; }
  .education li {
    font-size: 12.5px; line-height: 19.6px;
    padding-left: 12px; position: relative;
  }
  .education li::before {
    content: ""; position: absolute; left: 0; top: 7px;
    width: 7px; height: 6px; background: var(--accent);
    transform: skewY(-12deg);
  }
  .services {
    position: absolute; left: 402px; top: 497px; width: 440px;
    color: var(--muted);
  }
  .services h2 {
    font-size: 16px; font-weight: 700; color: var(--services-title);
    text-transform: uppercase; margin-left: 12px; margin-bottom: 10px;
  }
  .services ul { list-style: none; }
  .services li {
    font-size: 10.3px; line-height: 16px; color: #4d4d4d;
    padding-left: 12px; position: relative;
  }
  .services li::before {
    content: ""; position: absolute; left: 0; top: 5px;
    width: 7px; height: 6px; background: #666666;
    transform: skewY(-12deg);
  }
  .statistic {
    position: absolute; left: 370px; top: 704px; width: 400px;
    text-align: center; font-size: 14px; line-height: 18px; color: var(--ink);
  }
  .statistic strong { font-weight: 700; }
  .mission {
    position: absolute; left: 25px; top: 606px; width: 268px;
    font-size: 12px; line-height: 15.4px; color: #ffffff;
  }
</style>
</head>
<body>
  <main class="folder">
    <svg class="folder-shapes" width="1178" height="786" viewBox="0 0 1178 786" xmlns="http://www.w3.org/2000/svg">
      <defs>
        <linearGradient id="family-photo-tone" x1="0" y1="0" x2="1" y2="1">
          <stop offset="0" stop-color="#9bb07a"/>
          <stop offset="0.45" stop-color="#6f5545"/>
          <stop offset="1" stop-color="#2f3d5c"/>
        </linearGradient>
        <linearGradient id="couple-photo-tone" x1="0" y1="0" x2="1" y2="0">
          <stop offset="0" stop-color="#d9d0c0" stop-opacity="0"/>
          <stop offset="0.25" stop-color="#b8c9d6"/>
          <stop offset="1" stop-color="#d8d2cc"/>
        </linearGradient>
        <clipPath id="beige-clip">
          <path d="M443 396 L1073 563 Q1098 570 1093 592 L1048 786 L458 786 L353 748 Q340 740 343 718 L420 420 Q426 392 443 396 Z"/>
        </clipPath>
      </defs>

      <path class="band-top-left" d="M18 0 L513 0 L480 118 Q472 140 448 136 L30 22 Q18 18 18 0 Z" fill="var(--brown)"/>

      <path d="M20 54 L430 164 Q462 174 456 206 L366 562 Q358 586 333 580 L0 492 L0 70 Q0 50 20 54 Z"
            fill="url(#family-photo-tone)" role="img" aria-label="Photo of a smiling family of four"/>

      <path class="band-bottom-left" d="M0 520 L310 604 Q340 614 334 642 L298 786 L0 786 Z" fill="var(--brown)"/>

      <path class="panel-gray" d="M528 0 L1068 0 L1178 30 L1178 288 L1120 516 Q1112 542 1086 536 L463 368 Q440 360 445 336 L523 8 Z" fill="var(--gray-panel)"/>

      <path class="panel-beige" d="M443 396 L1073 563 Q1098 570 1093 592 L1048 786 L458 786 L353 748 Q340 740 343 718 L420 420 Q426 392 443 396 Z" fill="var(--beige-panel)"/>

      <rect x="775" y="500" width="330" height="290" fill="url(#couple-photo-tone)" clip-path="url(#beige-clip)"
            role="img" aria-label="Photo of a smiling senior couple embracing outdoors"/>

      <path class="edge-beige" d="M1178 368 L1116 600 Q1112 622 1134 628 L1178 640 Z" fill="var(--beige-panel)"/>
      <path class="edge-gray" d="M1110 650 L1178 668 L1178 786 L1063 786 L1094 664 Q1098 646 1110 650 Z" fill="var(--gray-panel)"/>
    </svg>

    <section class="intro">
      <p><strong>Good patient education can be invaluable to both physician and patient.</strong></p>
      <p>A patient who is educated about his or her health issues is far better prepared to work with their physician as a partner in managing their pain. Those patients are also more likely to have an internal locus - not expecting the doctor to "fix" everything, but relying on themselves as well. Understanding their medications equals better compliance.</p>
      <p>Educating your patients equals less opioid misuse and abuse and all of this leads to healthier and happier patients and makes treatment easier for their physicians.</p>
    </section>

    <section class="terms">
      <p class="terms-heading">Understanding Misunderstood Terms</p>
      <p><em>Physical Dependence:</em> withdrawal symptoms arise by abrupt cessation, rapid dose reduction or antagonist administered</p>
      <p><em>Tolerance:</em> Greater amount of drug needed to maintain therapeutic effect, or loss of effect over time.</p>
      <p><em>Pseudoaddiction:</em> behavior suggestive of addiction; caused by undertreatment of pain</p>
      <p><em>Addiction:</em> psychiatric disorder characterized by continued compulsive use of substance despite harm</p>
    </section>

    <section class="education">
      <h2>Opioid Education Testing</h2>
      <ul>
        <li>Using Opioids Safely</li>
        <li>The Role of Medications</li>
        <li>Opioid Agreements and Contracts</li>
        <li>Responsible Use</li>
        <li>Storing Medication</li>
        <li>Alcohol &amp; Marijuana and Pain Medication</li>
        <li>Over the counter Medication</li>
        <li>Storing your Medication Safely</li>
      </ul>
    </section>

    <section class="services">
      <h2>Services Provided</h2>
      <ul>
        <li>Pro-Active Opioid Education</li>
        <li>Screening for potential substance use disorders related to prescribed and non-prescribed</li>
        <li>Educating patients about the risks, warnings, and symptoms of over the counter medications</li>
        <li>Educational materials given to patients about the risk of taking medications inappropriately</li>
        <li>Assessment for substance use disorders related to medical issues and prescribed medications</li>
        <li>Counseling provided by highly trained, competent and experienced professionals.</li>
      </ul>
    </section>

    <p class="statistic">“Nearly a million emergency department visits in 2011 were due to <strong>People Misusing or Abusing Prescription</strong> painkillers”</p>

    <p class="mission">CareWell Counseling is dedicated to providing an unprecedented level of information, resources and educational support to your patients. We are committed to promoting a culture of transparency, documentation for doctors, meaningful interaction and active participation that will allow patients to assume a greater role in their healthcare through pro active addiction education, assessment, prevention, and screening</p>
  </main>
</body>
</html>
```